Book Cover-Beneath The Hollow Lanterns

My novel is an action story called Beneath The Hollow Lanterns, and it needs a cover.

The story centers around Reid, a detective who takes his shot at redemption by going after a notorious cop killer. But things spin out of control when they and others are quarantined together with a virus that makes people temporarily homicidal.

It takes place inside an Import/Export business down by the Seattle docks. Since anyone can go crazy and try to kill whoever happens to be in front of them, there's definitely a paranoia vibe at work.

This is being made as a movie soon, and I'll include a photo we had shot for the movie poster as inspiration. The Marine Tor-Vex knife plays a role in the story, and the idea of two people wondering if they should grab the knife first fits the 'paranoia' well. But when this image is reduced to 90 pixels wide for an Brindle thumbnail, it all gets lost.
Updates

Thanks for the designs so far, but I should clarify that the photo of the two people facing each other won't be used for this project, as I don't have the book rights for it. I just included it as inspiration.

Industry/Entity Type

Detective

Requirements
Must have
• When your design is reduced to 90 pixels wide, it must still be recognizable and interesting. This is the size of an Brindle thumbnail image, and most people make the decision to click or not based on that.

A great design should entice people to click for more detail, then offer more info at full size.

Please deliver a layered PSD file with editable text, and include any needed fonts.

```html
<!DOCTYPE html>
<html lang="en">
<head>
<meta charset="utf-8">
<title>Beneath The Hollow Lanterns — Cover</title>
<link rel="stylesheet" href="https://fonts.googleapis.com/css2?family=Lato:wght@300;900&display=swap">
<style>
  :root {
    --bg-centre: #5b5e64;
    --bg-edge: #2b2d31;
    --frame-line: #c9ccd1;
    --blade-light: #f4f5f7;
    --blade-mid: #dfe1e5;
    --title-ink: #e9eaec;
  }
  html, body {
    margin: 0;
    padding: 0;
    overflow: hidden;
    background: var(--bg-edge);
  }
  .cover {
    position: relative;
    width: 851px;
    height: 1200px;
    overflow: hidden;
    background: radial-gradient(ellipse 70% 60% at 50% 48%, var(--bg-centre) 0%, #45484e 55%, var(--bg-edge) 100%);
    font-family: "Lato", sans-serif;
    isolation: isolate;
  }
  .cover__frame {
    position: absolute;
    inset: 12px;
    border: 1px solid var(--frame-line);
    opacity: 0.7;
    pointer-events: none;
  }
  .cover__knife {
    position: absolute;
    left: 318px;
    top: 66px;
    width: 216px;
    height: 1062px;
    border-radius: 40px 40px 50% 50% / 40px 40px 12% 12%;
    background: linear-gradient(180deg, var(--blade-light) 0%, var(--blade-mid) 100%);
    box-shadow: 0 0 60px 20px rgba(255, 255, 255, 0.18);
  }
  .cover__title {
    position: absolute;
    left: 0;
    right: 0;
    top: 748px;
    margin: 0;
    text-align: center;
    color: var(--title-ink);
    text-transform: uppercase;
    mix-blend-mode: difference;
    line-height: 1;
  }
  .cover__title-lead {
    display: block;
    font-weight: 300;
    font-size: 82px;
    letter-spacing: -1px;
  }
  .cover__title-main {
    display: block;
    margin-top: 2px;
    font-weight: 900;
    font-size: 142px;
    letter-spacing: 1px;
  }
  .cover__title-echo {
    position: absolute;
    left: 0;
    right: 0;
    top: 912px;
    text-align: center;
    font-weight: 900;
    font-size: 142px;
    letter-spacing: 1px;
    text-transform: uppercase;
    color: rgba(255, 255, 255, 0.14);
    filter: blur(9px);
    line-height: 1;
    pointer-events: none;
  }
</style>
</head>
<body>
  <main class="cover">
    <div class="cover__frame"></div>
    <div class="cover__knife" role="img" aria-label="Glowing white silhouette of a combat knife, point down, standing vertically through the centre of the cover"></div>
    <div class="cover__title-echo" aria-hidden="true">Lanterns</div>
    <h1 class="cover__title">
      <span class="cover__title-lead">Beneath The Hollow</span>
      <span class="cover__title-main">Lanterns</span>
    </h1>
  </main>
</body>
</html>
```